Business Card Design Project

I need a business card design for my freelance solo makeup artistry business in Melbourne, Australia called Rosa Marindi. My freelance business specialises in bridal and special occassions makeup.

I like the idea of having Rosa Marindi in pink as its a feminine and soft colour. I would like a very clean, classy and simple (with an element of fun if that's possible) design. I would consider the business name to be in gloss with an otherwise matte finish.

Underneath the business name, I would like "Makeup by Tessa Colwick"

I do not want any bridal related graphics.

Target Market(s)

Young females with a disposable income from ages 20-40 and females getting married who will dictate who does mother of bride makeup ages 40-70.

Industry/Entity Type

Business

Requirements
Must have
• "Makeup by Tessa Colwick"

Ph: 0412 385 604
E: rosamarindi@inboxly.net
ABN: 58204917362
Nice to have
• I think I would like a mini business cards which is more slimline. I do like the colours of pink, white and grey but open to suggestions.
Should not have
• Bridal related graphics

```html
<!DOCTYPE html>
<html lang="en">
<head>
<meta charset="utf-8">
<title>Rosa Marindi – Slimline Business Cards</title>
<link rel="stylesheet" href="https://fonts.googleapis.com/css2?family=Dancing+Script:wght@600&family=Pinyon+Script&family=Arimo&display=swap">
<style>
  :root {
    --page-bg: #ecebee;
    --card-deep: #34387e;
    --card-mid: #3c4288;
    --card-glow: #5a70ad;
    --brand-pink: #e6449f;
    --text-white: #ffffff;
    --ornament-white: rgba(255, 255, 255, 0.55);
    --ornament-fade: rgba(255, 255, 255, 0);
  }
  * { margin: 0; padding: 0; box-sizing: border-box; }
  html, body {
    width: 1200px;
    height: 1000px;
    overflow: hidden;
    background: var(--page-bg);
  }
  .canvas {
    position: relative;
    width: 1200px;
    height: 1000px;
  }
  .card {
    position: absolute;
    left: 263px;
    width: 674px;
    border-radius: 18px;
    overflow: hidden;
    background:
      radial-gradient(ellipse 420px 200px at 72% 8%, var(--card-glow), transparent 70%),
      linear-gradient(180deg, var(--card-mid), var(--card-deep));
    box-shadow: 0 3px 10px rgba(0, 0, 0, 0.18);
    font-family: "Arimo", Arial, sans-serif;
    color: var(--text-white);
  }
  .card--script { top: 206px; height: 244px; }
  .card--formal { top: 500px; height: 238px; }

  .ornament {
    position: absolute;
    top: 0;
    height: 100%;
  }
  .ornament--left {
    left: 0;
    width: 230px;
    background:
      radial-gradient(circle 70px at 20px 45px, var(--ornament-white), var(--ornament-fade) 75%),
      radial-gradient(circle 55px at 145px 180px, var(--ornament-white), var(--ornament-fade) 75%),
      radial-gradient(circle 50px at 150px 10px, var(--ornament-white), var(--ornament-fade) 75%),
      radial-gradient(circle 45px at 0px 170px, var(--ornament-white), var(--ornament-fade) 75%);
  }
  .ornament--right {
    right: 0;
    width: 170px;
    background:
      radial-gradient(circle 65px at 105px 10px, var(--ornament-white), var(--ornament-fade) 75%),
      radial-gradient(circle 55px at 130px 125px, var(--ornament-white), var(--ornament-fade) 75%),
      radial-gradient(circle 50px at 50px 240px, var(--ornament-white), var(--ornament-fade) 75%);
  }

  .brand-name {
    position: absolute;
    color: var(--brand-pink);
    line-height: 1;
    white-space: nowrap;
  }
  .card--script .brand-name {
    left: 195px;
    top: 46px;
    font-family: "Dancing Script", cursive;
    font-weight: 600;
    font-size: 50px;
    letter-spacing: 1px;
  }
  .card--formal .brand-name {
    left: 199px;
    top: 38px;
    font-family: "Pinyon Script", cursive;
    font-size: 50px;
  }

  .tagline {
    position: absolute;
    left: 302px;
    font-size: 18px;
    line-height: 1;
    white-space: nowrap;
  }
  .card--script .tagline { top: 97px; }
  .card--formal .tagline { top: 95px; }

  .contact {
    position: absolute;
    list-style: none;
    font-size: 17px;
    line-height: 24px;
    white-space: nowrap;
  }
  .card--script .contact { left: 256px; top: 154px; }
  .card--formal .contact { left: 245px; top: 157px; }
</style>
</head>
<body>
<main class="canvas">

  <article class="card card--script">
    <div class="ornament ornament--left" role="img" aria-label="White brush-stroke swirl ornaments"></div>
    <div class="ornament ornament--right" role="img" aria-label="White brush-stroke swirl ornaments"></div>
    <h1 class="brand-name">Rosa Marindi</h1>
    <p class="tagline">Makeup by Tessa Colwick</p>
    <ul class="contact">
      <li>Ph: 0412 385 604</li>
      <li>E: rosamarindi@inboxly.net</li>
      <li>ABN: 58204917362</li>
    </ul>
  </article>

  <article class="card card--formal">
    <div class="ornament ornament--left" role="img" aria-label="White brush-stroke swirl ornaments"></div>
    <div class="ornament ornament--right" role="img" aria-label="White brush-stroke swirl ornaments"></div>
    <h2 class="brand-name">Rosa Marindi</h2>
    <p class="tagline">Makeup by Tessa Colwick</p>
    <ul class="contact">
      <li>Ph: 0412 385 604</li>
      <li>E: rosamarindi@inboxly.net</li>
      <li>ABN: 58204917362</li>
    </ul>
  </article>

</main>
</body>
</html>
```